Kalmoret Windham & Associates

We would like a simple, professional business card using a similar font to our logo.

Industry/Entity Type

Law Firm

Contact Information for Business Card

Martin Kalmoret, Esq. 47 Tillman Lane, 2nd Floor Harlow Falls, MA 02091 Office: 781.555.0143 Cell: 508.555.0196 Email: marty@kwfirmma.com kalmoretwindhamlaw.com

Font styles to use
Other font styles liked:
• We would like to use the fonts used in the logo or similar

Colors
0054AA
0677BA
7BADD7
CADEEF
E8F1F8

Requirements
Must have
• We would like the fonts to match the logo
Nice to have
• not too much design- very simple and professional business card. I added a picture of a business card that I tried to start but I am not a designer! Hopefully it will help with the address and phone numbers and kind of what we are looking for.

```html
<!DOCTYPE html>
<html lang="en">
<head>
<meta charset="utf-8">
<title>Kalmoret Windham &amp; Associates — Business Card</title>
<link rel="stylesheet" href="https://fonts.googleapis.com/css2?family=Cinzel:wght@400;600;700&family=Tinos&display=swap">
<style>
  :root {
    --navy: #233a70;
    --white: #ffffff;
    --grey-text: #6b6b6b;
    --backdrop: #ebeced;
    --shadow: rgba(0, 0, 0, 0.35);
  }
  html, body {
    margin: 0;
    padding: 0;
    width: 1200px;
    height: 1200px;
    overflow: hidden;
    background: var(--backdrop);
  }
  .canvas {
    position: relative;
    width: 1200px;
    height: 1200px;
    font-family: "Cinzel", serif;
  }
  .card {
    position: absolute;
    width: 872px;
    height: 510px;
    box-shadow: 6px 7px 6px var(--shadow);
  }
  .card--front {
    left: 178px;
    top: 42px;
    background: var(--navy);
    color: var(--white);
  }
  .card--back {
    left: 182px;
    top: 629px;
    background: var(--white);
    color: var(--navy);
  }
  .brand {
    position: absolute;
    display: flex;
    align-items: center;
  }
  .brand__square {
    flex: none;
  }
  .brand__name {
    margin: 0;
    font-weight: 700;
    line-height: 0.98;
  }
  .card--front .brand {
    left: 150px;
    top: 165px;
    gap: 145px;
  }
  .card--front .brand__square {
    width: 150px;
    height: 150px;
    background: var(--white);
  }
  .card--front .brand__name {
    font-size: 44px;
    color: var(--white);
  }
  .website {
    position: absolute;
    left: 0;
    right: 0;
    top: 426px;
    margin: 0;
    text-align: center;
    font-size: 24px;
    font-weight: 600;
    letter-spacing: 3.4px;
  }
  .card--back .brand {
    left: 71px;
    top: 40px;
    gap: 102px;
  }
  .card--back .brand__square {
    width: 90px;
    height: 90px;
    background: var(--navy);
  }
  .card--back .brand__name {
    font-size: 27px;
    color: var(--navy);
  }
  .person {
    position: absolute;
    left: 72px;
    top: 196px;
    margin: 0;
    font-size: 31px;
    font-weight: 600;
    letter-spacing: 0.5px;
  }
  .address {
    position: absolute;
    left: 74px;
    top: 285px;
    font-style: normal;
    font-size: 19px;
    font-weight: 600;
    line-height: 40px;
  }
  .contact {
    position: absolute;
    top: 390px;
    margin: 0;
    font-size: 19px;
    font-weight: 600;
    line-height: 40px;
  }
  .contact--phones { left: 78px; }
  .contact--online { left: 502px; }
  .contact__number {
    font-family: "Tinos", serif;
    font-weight: 400;
    color: var(--grey-text);
  }
</style>
</head>
<body>
<main class="canvas">
  <section class="card card--front" aria-label="Card front">
    <div class="brand">
      <span class="brand__square"></span>
      <p class="brand__name">Kalmoret<br>Windham<br>&amp; Associates</p>
    </div>
    <p class="website">www.Kalmoretwindhamlaw.com</p>
  </section>

  <section class="card card--back" aria-label="Card back">
    <div class="brand">
      <span class="brand__square"></span>
      <p class="brand__name">Kalmoret<br>Windham<br>&amp; Associates</p>
    </div>
    <h1 class="person">Martin Kalmoret, Esq</h1>
    <address class="address">
      47 Tillman Lane,<br>
      2nd Floor, Harlow Falls, MA 02091
    </address>
    <p class="contact contact--phones">
      OFFICE <span class="contact__number">(781.555.0143)</span><br>
      PHONE <span class="contact__number">(508.555.0196)</span>
    </p>
    <p class="contact contact--online">
      Marty@kwfirmma.com<br>
      Kalmoretwindhamlaw.com
    </p>
  </section>
</main>
</body>
</html>
```